Design Landing Page and User Interface for Online Second Hand Merchandice Store in Web 2.0 type pa

We are creating a company which delivers second hand merchandise locally. We'd like to have a landing page developed in the web 2.0 parallax scrolling web 2.0 style. We have a design style in mind. We need to have other pages within the website designed also. However, we need to get the landing page correct first.

In the center of the landing page, there will be the Second Hand Lantern Yard Lantern Yard logo. Underneath that logo, there will be an entry to enter your email and underneath that entry, there will be an entry to enter your password. Then there will be a login button. This will be the top layer of the landing page and it will be "transparent".

The second layer of the landing page, will be "behind" the logo and login. On this second layer, there will be boxes that will have pictures of items for sale such furniture, zelbits, lamps, books, CD's, TV, couches, beds. The boxes will flip over randomly and then the price for the item will be shown on the flip side of the box. If a user clicks on the box to find the price.

Scrolling down the landing Page – When you scroll down the landing page, you will see a little info graphic, which will show you how the service works. This is kind of an emulation of the Quillvane.com website which is pretty clean and looks nice.

At the bottom of the landing page you will have the menu that will have the same items as the Tundrelle landing page. This will pretty much allow users to get anywhere they need to in the site. This will also serve as a guide to you to how to design architect and build everything onward from here.

NOTE: THE LANDING PAGE WILL ONLY BE SKETCH PAGES 1-4

Target Market(s)

The customers will be hipsters who live in artsy neighborhoods in the United States. The customers are cost conscious and like to save money, but also appreciate style and are also very tech savvy. The ride bicycles and are into recycling and doing helping the environment.

Industry/Entity Type

Architect

Requirements
Must have
• The website design must have the parallax scrolling style. The landing page must have our company logo on it. The logo of the company name is attached in this brief. The logo reads Second Hand Lantern Yard.

Nice to have
• A cool modern look. Imagine if Blorvik opened up a Second Hand Goods store. That's what I want it to look like.
Should not have
• An early 2000's or mid 2000's style of design.

```html
<!DOCTYPE html>
<html lang="en">
<head>
<meta charset="utf-8">
<title>Ashgrove Lantern Yard</title>
<link href="https://fonts.googleapis.com/css2?family=Raleway:wght@400;500;600;700;800&family=Open+Sans:wght@400;600&display=swap" rel="stylesheet">
<style>
  :root {
    --teal: #1f6b6a;
    --maroon: #7a2622;
    --ink: #2b2b2b;
    --muted: #8a8a8a;
    --white: #ffffff;
    --band-light: #f2f2f2;
    --band-mid: #e2e2e2;
    --band-footer: #d2d2d2;
    --hero-warm: #f7d9a8;
    --hero-cool: #a9dcdc;
    --mosaic-dark: #6e5048;
    --mosaic-light: #b39a90;
  }
  * { box-sizing: border-box; margin: 0; padding: 0; }
  html, body { width: 940px; height: 1200px; overflow: hidden; }
  body {
    font-family: "Open Sans", Arial, sans-serif;
    color: var(--ink);
    background: var(--white);
    position: relative;
  }
  .section { position: absolute; left: 0; width: 940px; }
  .hero { top: 0; height: 338px; background: var(--white); }
  .hero-illustration {
    position: absolute; left: 100px; top: 20px; width: 720px; height: 318px;
    border-radius: 360px 360px 0 0;
    background: radial-gradient(ellipse at 50% 100%, var(--white) 0 38%, var(--hero-warm) 39%, var(--hero-cool) 75%, var(--white) 76%);
  }
  .features { top: 338px; height: 238px; background: var(--band-light); }
  .brand-badge {
    position: absolute; left: 350px; top: 210px; width: 240px; height: 240px;
    border-radius: 50%; background: var(--white); border: 6px solid var(--maroon);
    display: flex; align-items: center; justify-content: center; text-align: center;
    z-index: 2;
  }
  .brand-name {
    font-family: "Raleway", Arial, sans-serif; font-weight: 800; font-size: 30px;
    line-height: 1.1; color: var(--teal); text-transform: uppercase; letter-spacing: 1px;
  }
  .feature { position: absolute; width: 200px; }
  .feature h3 {
    font-family: "Raleway", Arial, sans-serif; font-weight: 600; font-size: 13px;
    display: flex; align-items: center; gap: 8px; margin-bottom: 8px;
  }
  .feature p { font-size: 9.5px; line-height: 1.55; color: var(--muted); }
  .feature.right { text-align: right; }
  .feature.right h3 { justify-content: flex-end; }
  .ring { width: 13px; height: 13px; border-radius: 50%; border: 3px solid var(--teal); flex: none; }
  .ring.maroon { border-color: var(--maroon); }
  .ring.filled { background: var(--maroon); border-color: #4a1614; }
  .f1 { left: 117px; top: 16px; }
  .f2 { left: 620px; top: 16px; }
  .f3 { left: 157px; top: 122px; }
  .f4 { left: 585px; top: 122px; }
  .cta { position: absolute; left: 367px; top: 134px; display: flex; align-items: center; gap: 6px; z-index: 3; }
  .btn {
    display: block; width: 98px; height: 30px; line-height: 30px; text-align: center;
    font-family: "Raleway", Arial, sans-serif; font-size: 11px; color: var(--white);
    text-decoration: none; border-radius: 2px;
  }
  .btn-login { background: var(--teal); }
  .btn-more { background: var(--maroon); }
  .cta-or { font-size: 9px; color: var(--muted); }
  .tagline {
    position: absolute; top: 184px; width: 100%; text-align: center;
    font-family: "Raleway", Arial, sans-serif; font-size: 21px; color: #555;
  }
  .tagline .buy { color: var(--teal); font-weight: 700; }
  .tagline .sell { color: var(--maroon); font-weight: 700; }
  .how { top: 576px; height: 207px; background: var(--band-mid); }
  .how-copy { position: absolute; left: 124px; top: 30px; width: 330px; }
  .how-copy h2 { font-family: "Raleway", Arial, sans-serif; font-weight: 500; font-size: 13px; margin-bottom: 10px; }
  .how-copy p { font-size: 9.5px; line-height: 1.6; color: var(--muted); }
  .video { position: absolute; left: 522px; top: 29px; width: 294px; height: 148px; border-radius: 4px; overflow: hidden; }
  .video-still { position: absolute; inset: 0; background: linear-gradient(120deg, #dcdcdc 0%, #9a9a9a 45%, #4a4a4a 100%); }
  .video-controls { position: absolute; left: 10px; right: 10px; bottom: 8px; height: 18px; }
  .testimonial { top: 783px; height: 86px; background: var(--band-light); text-align: center; }
  .testimonial blockquote { font-family: "Raleway", Arial, sans-serif; font-size: 15px; color: #444; margin-top: 22px; }
  .testimonial cite { display: block; font-style: normal; font-size: 8px; color: #444; margin-top: 8px; }
  .testimonial cite strong { font-weight: 600; }
  .community { top: 869px; height: 153px; background: linear-gradient(180deg, var(--mosaic-light), var(--mosaic-dark)); }
  .contact { top: 1022px; height: 116px; background: linear-gradient(180deg, var(--band-mid), #dadada); text-align: center; }
  .contact h2 { font-family: "Raleway", Arial, sans-serif; font-weight: 600; font-size: 13px; margin-top: 24px; }
  .contact p { font-size: 9px; color: var(--muted); margin-top: 8px; }
  .social { display: flex; justify-content: center; gap: 12px; margin-top: 12px; list-style: none; }
  .social li { display: flex; align-items: center; gap: 4px; font-size: 8px; color: var(--teal); }
  .social .dot { width: 14px; height: 14px; border-radius: 50%; background: var(--teal); }
  .footer { top: 1138px; height: 62px; background: var(--band-footer); }
  .footer-nav { display: flex; justify-content: center; gap: 24px; list-style: none; margin-top: 26px; }
  .footer-nav a { font-size: 9px; color: #777; text-decoration: none; }
</style>
</head>
<body>
  <header class="section hero">
    <div class="hero-illustration" role="img" aria-label="Colourful illustrated city skyline arching around the brand, with landmarks, hot air balloon, clouds and a plane"></div>
  </header>

  <div class="brand-badge">
    <span class="brand-name">Ashgrove<br>Lantern Yard</span>
  </div>

  <section class="section features">
    <div class="feature f1">
      <h3><span class="ring"></span>Post Your Staff To Sell</h3>
      <p>Lorem ipsum dolor sit amet, consectetur adipiscing elit. Mauris interdum velit vitae nulla molestie eu.</p>
    </div>
    <div class="feature right f2">
      <h3>Get Offers<span class="ring maroon"></span></h3>
      <p>Lorem ipsum dolor sit amet, consectetur adipiscing elit. Mauris interdum velit vitae nulla molestie eu.</p>
    </div>
    <div class="feature f3">
      <h3><span class="ring"></span>Another Great Feature</h3>
      <p>Lorem ipsum dolor sit amet, consectetur adipiscing elit. Mauris interdum velit vitae nulla molestie eu.</p>
    </div>
    <div class="feature f4">
      <h3>Another Great Feature<span class="ring filled"></span></h3>
      <p>Lorem ipsum dolor sit amet, consectetur adipiscing elit. Mauris interdum velit vitae nulla molestie eu.</p>
    </div>
    <div class="cta">
      <a class="btn btn-login" href="#">LOGIN</a>
      <span class="cta-or">or</span>
      <a class="btn btn-more" href="#">Learn more</a>
    </div>
    <p class="tagline"><span class="buy">Buy</span> and <span class="sell">Sell</span> stuff to people who known people you known.</p>
  </section>

  <section class="section how">
    <div class="how-copy">
      <h2>How It's Works</h2>
      <p>Lorem ipsum dolor sit amet, consectetur adipiscing elit. Suspendisse fringilla fringilla nisl congue congue. Maecenas nec condimentum libero, at elementum mauris. Phasellus eget nisi dapibus, ultricies nisl at, hendrerit risusuis ornare luctus id sollicitudin ante lobortis at.</p>
    </div>
    <div class="video">
      <div class="video-still" role="img" aria-label="Misty black and white mountain valley video still"></div>
      <svg class="video-controls" viewBox="0 0 274 18" width="274" height="18" aria-hidden="true">
        <rect x="0" y="0" width="274" height="18" rx="2" fill="#1c1c1c" opacity="0.85"/>
        <path d="M9 5 L15 9 L9 13 Z" fill="#ffffff"/>
        <rect x="26" y="7.5" width="200" height="3" fill="#555"/>
        <rect x="26" y="7.5" width="92" height="3" fill="#2fa3d8"/>
        <rect x="234" y="6" width="14" height="6" fill="#2fa3d8"/>
        <rect x="256" y="5" width="8" height="8" fill="none" stroke="#ffffff" stroke-width="1.2"/>
      </svg>
    </div>
  </section>

  <section class="section testimonial">
    <blockquote>"Simply and extremely affordable I would reccomend it to anyone."</blockquote>
    <cite><strong>Miro Castell,</strong> Blogger</cite>
  </section>

  <section class="section community" role="img" aria-label="Sepia-toned mosaic of member portrait photos"></section>

  <section class="section contact">
    <h2>Say Hi &amp; Get in Touch</h2>
    <p>Lorem ipsum dolor sit amet, consectetur adipiscing elit suspendisse.</p>
    <ul class="social">
      <li><span class="dot"></span>Blorvik</li>
      <li><span class="dot"></span>Facemoor</li>
      <li><span class="dot"></span>Pinwell</li>
      <li><span class="dot"></span>Glimmo</li>
      <li><span class="dot"></span>Linkary</li>
      <li><span class="dot"></span>Vidora</li>
    </ul>
  </section>

  <footer class="section footer">
    <ul class="footer-nav">
      <li><a href="#">Contact</a></li>
      <li><a href="#">Download</a></li>
      <li><a href="#">Press</a></li>
      <li><a href="#">Email</a></li>
      <li><a href="#">Support</a></li>
      <li><a href="#">Privacy Policy</a></li>
    </ul>
  </footer>
</body>
</html>
```